Business Card Design - Construction Company

Tarrowin Construction is in need of a sharp, modern business card design that has an architectural/high fashion feel.

We are looking for a two sided card.

One side simple dark grey/black with some texture in the background. e.g. (a mosaic of simple interconnecting shapes or a shadow of the logo.) Something to draw attention and create interest.It will need to feature a large Tarrowin construction logo (files attached) in metallic gradient or plain white.

The other side should contain all of our information:

(in largest text)
Name of person
Tarrowin Construction Pty. Ltd.

Licensed builders specialising in:
- Bathrooms
- Kitchens
- Commercial interiors

(mid sized text)
Phone number
Fax number
person@tarrowinconstruction.example.au
www. tarrowinconstruction.example.au

(smaller text)
ABN: 62407938215
BSA license: xxx-xxxx
PO Box 8641 Kellsmoor QLD 4019 (address)

Target Market(s)

professional home and business owners

Industry/Entity Type

Construction

Requirements
Must have
• Must be bold, professional looking and modern.
Nice to have
• We are undecided as to what kind of printing we will go with.
Definitely square edged.
Probably high quality satin card.
We are also interested in designs that would work well on transparent or translucent plastic.
Ideally we would print two versions.
Should not have
• Nothing with an antique feel.
No wild colours. Small amounts of colour can be good in the right place.

```html
<!DOCTYPE html>
<html lang="en">
<head>
<meta charset="utf-8">
<title>Tarrowin Construction – Business Card</title>
<link href="https://fonts.googleapis.com/css2?family=Open+Sans:ital,wght@0,400;0,600;1,400&display=swap" rel="stylesheet">
<style>
  :root {
    --page: #ffffff;
    --card-dark: #050505;
    --card-light: #ffffff;
    --card-edge: #e4e4e4;
    --ink: #1c1c1c;
    --ink-soft: #333333;
    --accent: #2f86c8;
    --brand-text: #c9ccd0;
    --dash: #8a8a8a;
  }
  * { box-sizing: border-box; margin: 0; padding: 0; }
  html, body {
    width: 800px; height: 1200px; overflow: hidden;
    background: var(--page);
    font-family: "Open Sans", Arial, sans-serif;
    color: var(--ink);
  }
  .canvas { position: relative; width: 800px; height: 1200px; }

  .card { position: absolute; width: 624px; height: 352px; }

  /* Front */
  .card-front {
    left: 84px; top: 134px;
    background: var(--card-dark);
  }
  .brand {
    position: absolute; left: 0; right: 0; top: 120px;
    display: flex; align-items: center; justify-content: center; gap: 18px;
  }
  .brand-dot {
    width: 44px; height: 44px; border-radius: 50%;
    background: var(--accent);
  }
  .brand-name {
    font-weight: 600; font-size: 34px; letter-spacing: 1px;
    color: var(--brand-text);
  }
  .floor-glow { position: absolute; left: 212px; top: 282px; }

  /* Back */
  .card-back {
    left: 80px; top: 646px;
    background: var(--card-light);
    border: 1px solid var(--card-edge);
  }
  .company {
    position: absolute; left: 18px; top: 14px;
    font-size: 22px; color: var(--ink);
  }
  .person {
    position: absolute; left: 416px; top: 88px;
    font-size: 21px; color: var(--ink);
  }
  .services {
    position: absolute; left: 28px; top: 86px;
    width: 262px; height: 158px;
    border: 2px dashed var(--dash); border-radius: 14px;
    padding: 12px 14px;
    font-style: italic; font-size: 21px; line-height: 25px; color: var(--ink);
  }
  .legal {
    position: absolute; left: 18px; top: 278px;
    font-size: 13px; line-height: 24px; color: var(--ink-soft);
  }
  .contact {
    position: absolute; left: 304px; top: 254px;
    font-size: 16px; line-height: 24px; color: var(--ink);
  }
</style>
</head>
<body>
<main class="canvas">
  <section class="card card-front" aria-label="Business card front">
    <div class="brand">
      <span class="brand-dot" aria-hidden="true"></span>
      <span class="brand-name">Tarrowin Construction</span>
    </div>
    <svg class="floor-glow" width="200" height="30" viewBox="0 0 200 30" aria-hidden="true">
      <defs>
        <radialGradient id="glow" cx="50%" cy="50%" r="50%">
          <stop offset="0" stop-color="#ffffff"/>
          <stop offset="0.6" stop-color="#bdbdbd" stop-opacity="0.7"/>
          <stop offset="1" stop-color="#050505" stop-opacity="0"/>
        </radialGradient>
      </defs>
      <ellipse cx="100" cy="15" rx="98" ry="12" fill="url(#glow)"/>
    </svg>
  </section>

  <section class="card card-back" aria-label="Business card back">
    <h1 class="company" style="font-weight:400">Tarrowin Construction Pty. Ltd.</h1>
    <p class="person">Name of person</p>
    <div class="services">
      Licensed builders<br>specialising in:<br>- Bathrooms<br>- Kitchens<br>- Commercial interiors
    </div>
    <p class="legal">
      ABN: 62407938215<br>
      BSA license: xxx-xxxx<br>
      PO Box 8641 Kellsmoor QLD 4019
    </p>
    <p class="contact">
      Phone : 1234 5678<br>
      Fax : 1234 5678<br>
      person@tarrowinconstruction.example.au<br>
      www. tarrowinconstruction.example.au
    </p>
  </section>
</main>
</body>
</html>
```